Cosmetics Brand Logo and Bottle Label Design

We are creating a new cosmetics brand called "Nolan Whitby" and would like you to create an amazing logo and bottle label for this brand's new 100% pure argan oil product.
For the logo, we really like the logo's of Marin Calloway and Vessa. The text should be Sans Serif (without feet).
For the actual bottle label, please find attached labels of one of our competitors design which really like. We really like the simplicity and elegance of the design. The only difference is that our product will be using light turqoise as the brand color. Please feel free to add your own creativity into it as well.
Industry/Entity Type
Cosmetics
Logo Text
Nolan Whitby
Font styles to use

```html
<!DOCTYPE html>
<html lang="en">
<head>
<meta charset="utf-8">
<title>Nolan Whitby – Argan Oil Label</title>
<link href="https://fonts.googleapis.com/css2?family=Josefin+Sans:wght@200;300&family=Didact+Gothic&display=swap" rel="stylesheet">
<style>
  :root {
    --board: #231f20;
    --paper: #ffffff;
    --turquoise: #55c3d1;
    --cream: #f3f2d9;
    --amber-dark: #3a1606;
    --amber: #8a3a12;
  }
  html, body { margin: 0; padding: 0; overflow: hidden; }
  .board {
    position: relative;
    width: 1200px; height: 994px;
    background: var(--board);
    overflow: hidden;
  }
  .label {
    position: absolute;
    left: 55px; width: 613px; height: 430px;
  }
  .label--white { top: 45px; background: var(--paper); color: var(--turquoise); }
  .label--teal { top: 517px; background: var(--turquoise); color: var(--paper); }

  .wordmark {
    position: absolute; left: 0; right: 0; top: 56px;
    text-align: center;
    font-family: "Josefin Sans", sans-serif;
    font-weight: 200;
    font-size: 51px;
    letter-spacing: 1px;
    line-height: 1;
    white-space: nowrap;
  }
  .tagline {
    position: absolute; left: 0; right: 0; top: 119px;
    text-align: center;
    font-family: "Didact Gothic", sans-serif;
    font-size: 20px;
    letter-spacing: 2.8px;
    white-space: nowrap;
  }
  .details {
    position: absolute; left: 118px; top: 213px;
    writing-mode: vertical-rl;
    font-family: "Didact Gothic", sans-serif;
    font-size: 16px;
    line-height: 16px;
    letter-spacing: 2px;
    white-space: nowrap;
  }
  .brand-seal {
    position: absolute; left: 360px; top: 213px;
    width: 160px; height: 160px; border-radius: 50%;
    display: flex; align-items: center; justify-content: center;
    font-family: "Didact Gothic", sans-serif;
    font-size: 19px; letter-spacing: 1px;
  }
  .label--white .brand-seal { background: var(--turquoise); color: var(--paper); }
  .label--teal .brand-seal { background: var(--paper); color: var(--turquoise); }

  .mockup {
    position: absolute; left: 729px; top: 45px;
    width: 410px; height: 900px;
    background: var(--cream);
  }
  .bottle-photo {
    position: absolute; left: 61px; top: 15px;
    width: 292px; height: 820px;
    border-radius: 60px 60px 40px 40px;
    background: linear-gradient(90deg, var(--amber-dark), var(--amber) 45%, var(--amber-dark));
  }
  .bottle-label {
    position: absolute; left: 61px; top: 425px;
    width: 292px; height: 355px;
    background: var(--paper);
    color: var(--turquoise);
  }
  .bottle-label__titles {
    position: absolute; left: 28px; top: 42px; height: 294px;
    writing-mode: vertical-rl;
    transform: rotate(180deg);
    white-space: nowrap;
    overflow: hidden;
  }
  .bottle-label__wordmark {
    font-family: "Josefin Sans", sans-serif;
    font-weight: 200; font-size: 37px; letter-spacing: 0.5px;
    line-height: 42px;
  }
  .bottle-label__tagline {
    font-family: "Didact Gothic", sans-serif;
    font-size: 13.5px; letter-spacing: 2.2px; line-height: 20px;
  }
  .bottle-label__seal {
    position: absolute; left: 141px; top: 41px;
    width: 110px; height: 110px; border-radius: 50%;
    background: var(--turquoise); color: var(--paper);
    display: flex; align-items: center; justify-content: center;
    font-family: "Didact Gothic", sans-serif; font-size: 13px;
  }
  .bottle-label__details {
    position: absolute; left: 141px; top: 295px;
    font-family: "Didact Gothic", sans-serif;
    font-size: 11px; line-height: 13px; letter-spacing: 0.8px;
    white-space: nowrap;
  }
</style>
</head>
<body>
<div class="board">

  <section class="label label--white">
    <div class="wordmark">NOLAN WHITBY</div>
    <div class="tagline">100%Pure Argan Oil Light</div>
    <div class="details">ultra lightweight<br>moisturizing oil<br>120mL 4 fl.oz.</div>
    <div class="brand-seal">Nolan Whitby</div>
  </section>

  <section class="label label--teal">
    <div class="wordmark">NOLAN WHITBY</div>
    <div class="tagline">100%Pure Argan Oil Light</div>
    <div class="details">ultra lightweight<br>moisturizing oil<br>120mL 4 fl.oz.</div>
    <div class="brand-seal">Nolan Whitby</div>
  </section>

  <section class="mockup">
    <div class="bottle-photo" role="img" aria-label="Amber glass dropper bottle with black dropper cap"></div>
    <div class="bottle-label">
      <div class="bottle-label__titles">
        <div class="bottle-label__wordmark">NOLAN WHITBY</div>
        <div class="bottle-label__tagline">100%Pure Argan Oil Light</div>
      </div>
      <div class="bottle-label__seal">Nolan Whitby</div>
      <div class="bottle-label__details">ultra lightweight<br>moisturizing oil<br>120mL&nbsp; 4 fl.oz.</div>
    </div>
  </section>

</div>
</body>
</html>
```